6x9 Postcard Design Project

I have a web design and marketing company. I need a 6x9 postcard designed that grabs attention and tells all my services.

I have launched a new "Website Leasing" plan that allows small businesses to have a professionally designed website for an small down and a monthly payment. I want one side of the card to be about the leasing plan and its pricing.

I would also like all my services included.

Web Design
Search Engine Optimization
Social Media Services
Graphic Design
Video Production
IT Services
Low Monthly Pricing!

For more information about the leasing plan and all my services please use the content on:

www.plumvexo.com

I would like the design to follow my website color scheme BUT NOT THAT SAME LOOK AS MY WEBSITE, I am looking for creativity. I am open to other colors as well. Again, please do not make the design look like my website, I need something I can't do.

The final design files should also have a PSD so I can edit it as my services and prices change.

The final design should present my company as a professional, current and savvy design firm.

I am located in Mesa, Arizona
I serve Phoenix, Mesa, Gilbert, Chandler and all of Arizona.

Marcus
480-555-0173
Updates

This will be mailed out so it will need the appropriate area for the post office info

Hello,

I uploaded two templates that show the post office guidelines in regards to where the the ink free areas need to go. Thanks,

Marcus

Target Market(s)

Small/Medium Businesses

Industry/Entity Type

Graphic Design

Requirements
Must have
• Must have a place for the post office mailing info.
Nice to have
• A unique design that does not emulate my current website
Should not have
• It should not look like my website. I need a postcard design that is unique and not a clone of my site.

```html
<!DOCTYPE html>
<html lang="en">
<head>
<meta charset="utf-8">
<title>Plumvexo Website Leasing Postcard</title>
<link rel="stylesheet" href="https://fonts.googleapis.com/css2?family=Didact+Gothic&family=Archivo+Black&family=Tinos:wght@400;700&display=swap">
<style>
  :root {
    --page: #e9e6e1;
    --blue-deep: #1f5f93;
    --blue-mid: #2f7fbf;
    --blue-glow: #58bff0;
    --ink: #050505;
    --white: #ffffff;
    --sky-text: #62c6f2;
    --lime: #8dc63f;
    --grey-brand: #8a8a8a;
    --bullet-red: #e0332b;
    --social-blue: #4aa8e0;
    --social-navy: #3b4f9a;
  }
  * { margin: 0; padding: 0; box-sizing: border-box; }
  html, body { width: 1200px; height: 900px; overflow: hidden; background: var(--page); }
  body { position: relative; font-family: "Didact Gothic", Arial, sans-serif; }

  .card {
    position: absolute; top: 105px; width: 460px; height: 690px; overflow: hidden;
    background: radial-gradient(ellipse at 55% 42%, var(--blue-glow) 0%, var(--blue-mid) 38%, var(--blue-deep) 100%);
    box-shadow: 0 10px 28px rgba(0,0,0,.25);
  }
  .card--front { left: 70px; }
  .card--back { left: 670px; }
  .card svg.shapes { position: absolute; inset: 0; }

  /* front */
  .hero-art { position: absolute; left: 0; top: 0; width: 235px; height: 150px;
    background: linear-gradient(135deg, #0b1a22, #132f1f 60%, #0d2230); }
  .plan-rule { position: absolute; left: 135px; top: 150px; width: 325px; height: 47px;
    border-left: 1.5px solid var(--ink); border-bottom: 1.5px solid var(--ink); }
  .plan-title { position: absolute; right: 28px; top: 170px; color: var(--white); font-size: 18px; letter-spacing: .5px; }
  .intro { position: absolute; left: 25px; top: 216px; color: var(--white); font-size: 18.5px; line-height: 25px; letter-spacing: 1.2px; }
  .intro .brand-inline { color: var(--grey-brand); }
  .pricing { position: absolute; left: 210px; top: 348px; font-family: "Tinos", "Times New Roman", serif; font-size: 13.5px; line-height: 20px; }
  .pricing .down { color: var(--sky-text); }
  .pricing .monthly { color: var(--lime); }
  .benefits { position: absolute; left: 38px; top: 452px; width: 400px; color: var(--white); }
  .benefits h2 { font-family: "Archivo Black", Arial, sans-serif; font-size: 13px; font-weight: 400; letter-spacing: .5px; margin: 0 0 6px 12px; }
  .benefits ul { list-style: none; font-family: "Tinos", "Times New Roman", serif; font-size: 11px; line-height: 15px; }
  .benefits li { position: relative; padding-left: 12px; }
  .benefits li::before { content: ""; position: absolute; left: 1px; top: 5px; width: 6px; height: 6px; border-radius: 50%; background: var(--bullet-red); }
  .hl-lime { color: var(--lime); }
  .hl-blue { color: var(--social-blue); }
  .hl-navy { color: var(--social-navy); }
  .signature { position: absolute; left: 0; right: 0; top: 598px; text-align: center; }
  .signature .brand-name { color: var(--grey-brand); font-size: 36px; line-height: 36px; letter-spacing: -.5px; }
  .contact-row { position: absolute; left: 50px; right: 26px; top: 665px; display: flex; justify-content: space-between; align-items: baseline; font-size: 12px; }
  .contact-row .phone { color: var(--social-blue); }
  .contact-row .web { color: var(--white); font-size: 13px; }
  .contact-row .email { color: var(--lime); }

  /* back */
  .extras-title { position: absolute; left: 40px; top: 40px; font-family: "Archivo Black", Arial, sans-serif; font-size: 20px; color: var(--ink); }
  .extras-list { position: absolute; left: 0; right: 0; top: 82px; list-style: none; text-align: center; color: var(--white); font-size: 20px; line-height: 27px; letter-spacing: 1.5px; }
  .stamp { position: absolute; left: 330px; top: 430px; width: 80px; height: 80px; border: 1.5px solid var(--ink); }
  .address { position: absolute; left: 30px; top: 525px; width: 400px; height: 62px; border: 1.5px solid var(--ink); }
  .back-brand { position: absolute; left: 110px; top: 612px; color: var(--grey-brand); font-size: 22px; }
  .back-web { position: absolute; left: 100px; top: 645px; color: #333; font-size: 13px; letter-spacing: .5px; }
</style>
</head>
<body>

<section class="card card--front">
  <div class="hero-art" role="img" aria-label="Large word-cloud lettering of business words such as success, questions, team and achieved"></div>
  <svg class="shapes" width="460" height="690" viewBox="0 0 460 690" aria-hidden="true">
    <path d="M27 690 L27 395 L102 395 C150 330 260 300 460 298 L460 690 Z" fill="var(--ink)"/>
  </svg>
  <div class="plan-rule"></div>
  <p class="plan-title">Website leasing plan</p>
  <p class="intro">Expand your business by getting a<br>Website on installments through <span class="brand-inline">Plumvexo</span></p>
  <div class="pricing">
    <p class="down">Website DownPayment =$499 only</p>
    <p class="monthly">Monthly Installments= $249 only</p>
  </div>
  <div class="benefits">
    <h2>What You Get:</h2>
    <ul>
      <li>A new Website to expand your business beyond limits</li>
      <li>Regular Content-updates on existing Web-pages.</li>
      <li>Local On-Page <span class="hl-lime">Search Engine Optimization(SEO)</span></li>
      <li>Customized Social Media Setup For <span class="hl-blue">Chirpline</span> And <span class="hl-navy">Friendwall</span></li>
      <li>Local Searchly Places Account Set Up</li>
      <li>Annual <span class="hl-lime">“Facelift”</span> for keeping your website with the latest looks in the Website industry.</li>
    </ul>
  </div>
  <div class="signature">
    <p class="brand-name">Plumvexo</p>
  </div>
  <div class="contact-row">
    <span class="phone">(480) 555-0173</span>
    <span class="web">www.plumvexo.com</span>
    <span class="email">hello@plumvexo.com</span>
  </div>
</section>

<section class="card card--back">
  <svg class="shapes" width="460" height="690" viewBox="0 0 460 690" aria-hidden="true">
    <path d="M18 670 L18 410 Q18 362 68 362 C210 366 330 392 442 420 L442 670 Z" fill="var(--white)"/>
  </svg>
  <h2 class="extras-title">What else we can do for you:</h2>
  <ul class="extras-list">
    <li>Website Designing</li>
    <li>Graphics Designing</li>
    <li>Search Engine Optimization</li>
    <li>Social Media Services</li>
    <li>Video Production</li>
    <li>IT Services</li>
    <li>Low Monthly Pricing</li>
  </ul>
  <div class="stamp"></div>
  <div class="address"></div>
  <p class="back-brand">Plumvexo</p>
  <p class="back-web">www.plumvexo.com</p>
</section>

</body>
</html>
```